Business card design needed

I am looking for a simple but elegant business card that has a professional and a classy look and feel about it. Must engage the persons attention.
I own and run multiple dental practices and offer basic to advanced dentistry.

Target Market(s)

people looking for dentists

Industry/Entity Type

Dental

Contact Information for Business Card

Dr. Leopold Harwick
Bluefern Dental
Your Smile My Passion
Larkfield - 14 Tindale Street Ph: 0749511862
Brayton - 27 Corbel Street Ph: 0749306417
Millbrook - Shop 3 42 Pellow Drive Ph: 49628473
Email: lh@blueferndental.com.au

Requirements
Must have
• Contact Details
QR codes for easy storage and website redirection
email and web address

```html
<!DOCTYPE html>
<html lang="en">
<head>
<meta charset="utf-8">
<title>Bluefern Dental – Business Card</title>
<link rel="stylesheet" href="https://fonts.googleapis.com/css2?family=Arimo&family=Tinos:ital,wght@0,400;0,700;1,400&display=swap">
<style>
  :root {
    --page: #ffffff;
    --deep-green: #00565a;
    --teal: #17908e;
    --ink: #111111;
    --white: #ffffff;
    --edge: #000000;
  }
  * { box-sizing: border-box; margin: 0; padding: 0; }
  html, body { width: 1200px; height: 590px; overflow: hidden; background: var(--page); }
  .canvas { position: relative; width: 1200px; height: 590px; }

  .card {
    position: absolute;
    width: 363px; height: 209px;
    border: 1px solid var(--edge);
    overflow: hidden;
  }

  /* Front */
  .card--front { left: 227px; top: 104px; background: var(--white); }
  .brand {
    position: absolute; left: 58px; top: 22px;
    display: flex; align-items: center; gap: 10px;
  }
  .brand__mark {
    width: 56px; height: 56px; border-radius: 50%;
    border: 2px solid var(--teal);
  }
  .brand__name {
    font-family: "Tinos", "Times New Roman", serif;
    font-weight: 700; font-size: 29px; color: var(--teal);
    white-space: nowrap;
  }
  .tagline {
    position: absolute; left: 0; right: 0; top: 101px;
    text-align: center;
    font-family: "Arimo", Arial, sans-serif; font-size: 15px; color: var(--ink);
  }
  .tagline__accent { color: var(--teal); }
  .name-band {
    position: absolute; left: 0; right: 0; bottom: 0; height: 52px;
    background: var(--deep-green);
    display: flex; align-items: center; justify-content: center;
    font-family: "Tinos", "Times New Roman", serif; font-size: 28px; color: var(--white);
  }

  /* Back */
  .card--back { left: 677px; top: 102px; background: var(--deep-green); }
  .motto-strip {
    position: absolute; left: 0; top: 0; bottom: 0; width: 41px;
    background: var(--white);
    display: flex; align-items: center; justify-content: center;
  }
  .motto {
    transform: rotate(-90deg);
    white-space: nowrap;
    font-family: "Tinos", "Times New Roman", serif; font-style: italic;
    font-size: 19px; color: var(--ink);
  }
  .rule { position: absolute; top: 0; bottom: 0; }
  .rule--teal-a { left: 41px; width: 3px; background: var(--teal); }
  .rule--gap-a { left: 44px; width: 4px; background: var(--white); }
  .rule--teal-b { left: 48px; width: 5px; background: var(--teal); }
  .rule--gap-b { left: 53px; width: 2px; background: var(--white); }

  .contact {
    position: absolute; left: 121px;
    font-family: "Arimo", Arial, sans-serif; font-size: 11.5px; color: var(--white);
    display: flex; align-items: center; gap: 4px; white-space: nowrap;
  }
  .contact svg { flex: none; }
</style>
</head>
<body>
<div class="canvas">

  <section class="card card--front">
    <div class="brand">
      <span class="brand__mark"></span>
      <span class="brand__name">Bluefern Dental</span>
    </div>
    <p class="tagline">Beautiful <span class="tagline__accent">smiles</span> are made here</p>
    <div class="name-band">Dr. Leopold Harwick</div>
  </section>

  <section class="card card--back">
    <div class="motto-strip"><span class="motto">Your Smile, My Passion..!</span></div>
    <span class="rule rule--teal-a"></span>
    <span class="rule rule--gap-a"></span>
    <span class="rule rule--teal-b"></span>
    <span class="rule rule--gap-b"></span>

    <p class="contact" style="top:46px">Larkfield – 14 Tindale Street</p>
    <p class="contact" style="top:61px">
      <svg width="13" height="13" viewBox="0 0 13 13" aria-hidden="true"><circle cx="6.5" cy="6.5" r="6.5" fill="#fff"/><path d="M4 3.2c.4-.3.8-.2 1 .2l.6 1.2c.1.3 0 .6-.2.8l-.4.3c.3.8.9 1.5 1.7 1.9l.4-.4c.2-.2.5-.3.8-.1l1.1.6c.4.2.5.6.2 1-.5.7-1.2 1-2 .7C5.4 8.7 4.2 7.5 3.6 5.6c-.3-.9 0-1.8.4-2.4z" fill="#00565a"/></svg>
      0749511862
    </p>

    <p class="contact" style="top:93px">Brayton – 27 Corbel Street</p>
    <p class="contact" style="top:108px">
      <svg width="13" height="13" viewBox="0 0 13 13" aria-hidden="true"><circle cx="6.5" cy="6.5" r="6.5" fill="#fff"/><path d="M4 3.2c.4-.3.8-.2 1 .2l.6 1.2c.1.3 0 .6-.2.8l-.4.3c.3.8.9 1.5 1.7 1.9l.4-.4c.2-.2.5-.3.8-.1l1.1.6c.4.2.5.6.2 1-.5.7-1.2 1-2 .7C5.4 8.7 4.2 7.5 3.6 5.6c-.3-.9 0-1.8.4-2.4z" fill="#00565a"/></svg>
      0749306417
    </p>

    <p class="contact" style="top:140px">Millbrook - Shop 3 42 Pellow Drive</p>
    <p class="contact" style="top:155px">
      <svg width="13" height="13" viewBox="0 0 13 13" aria-hidden="true"><circle cx="6.5" cy="6.5" r="6.5" fill="#fff"/><path d="M4 3.2c.4-.3.8-.2 1 .2l.6 1.2c.1.3 0 .6-.2.8l-.4.3c.3.8.9 1.5 1.7 1.9l.4-.4c.2-.2.5-.3.8-.1l1.1.6c.4.2.5.6.2 1-.5.7-1.2 1-2 .7C5.4 8.7 4.2 7.5 3.6 5.6c-.3-.9 0-1.8.4-2.4z" fill="#00565a"/></svg>
      49628473
    </p>

    <p class="contact" style="top:182px">
      <svg width="15" height="11" viewBox="0 0 15 11" aria-hidden="true"><rect x="0.5" y="0.5" width="14" height="10" fill="#fff" stroke="#cfd8d8"/><path d="M0.5 0.5l7 5.5 7-5.5M0.5 10.5l5-4.5M14.5 10.5l-5-4.5" fill="none" stroke="#8a9a9a" stroke-width="0.8"/></svg>
      lh@blueferndental.com.au
    </p>
  </section>

</div>
</body>
</html>
```